IT Management and Consulting company wants a design

The website should transfer an innovative, forward-oriented, optimistic, and serious image to my customer. Because we work in an agile, the design should transfer this approach.

The new color should make a serious, but not boring, impression for the business visitors of top-level companies.

The main focus topics are:
* IT strategy consulting
* Digital transformation
* IT quality management

The website should be in the English language.

The website should be created for WordPress. The existing website is http://www.quorva-advisory.com (no WordPress) is provided by servalink.de. A WordPress sandbox system exists.

Target Market(s)

Purchasing departments, IT decision makers from companies, project recruiting companies

Industry/Entity Type

IT-Provider, Telecommunication, Automotive

Number of Pages Required

4 page

Font styles to use
Serif
Sans Serif

Requirements
Must have
• Long-pager scrolling, a detail page for each portfolio topics, contact page, page about the company
Nice to have
• Parallax animation less is more, maybe a nice Hero Video Header, interessting 3D graph, Isometric graphs will bi nice, more clean than overloaded,
Should not have
• personal recruting page like in www.quorva-advisory.com

```html
<!DOCTYPE html>
<html lang="en">
<head>
<meta charset="utf-8">
<title>Quorva Advisory – IT Management and Consulting</title>
<link href="https://fonts.googleapis.com/css2?family=Montserrat:wght@500;600;700;800&family=Open+Sans:wght@400;600;700&display=swap" rel="stylesheet">
<style>
:root{
  --gold:#f4b400;
  --gold-dark:#d99c00;
  --ink:#2f2f2f;
  --ink-soft:#555;
  --muted:#8a8a8a;
  --dark:#353535;
  --dark-2:#5c5c5c;
  --paper:#ffffff;
  --canvas:#ededed;
  --grey-band:#e6e6e6;
  --line:#dcdcdc;
}
*{box-sizing:border-box;margin:0;padding:0}
html,body{width:1200px;height:4800px;overflow:hidden}
body{background:var(--canvas);font-family:"Open Sans",Arial,sans-serif;color:var(--ink);font-size:14px;line-height:1.6}
h1,h2,h3,h4,.brand,.btn,.nav a,.stat-num{font-family:"Montserrat",Arial,sans-serif}
.site{position:absolute;left:100px;top:150px;width:1000px;background:var(--paper);box-shadow:0 0 18px rgba(0,0,0,.08)}
.btn{display:inline-block;background:var(--gold);color:#fff;font-weight:700;font-size:12px;padding:9px 20px;border-radius:2px;text-transform:uppercase;letter-spacing:.5px}
.eyebrow{font-family:"Montserrat",Arial,sans-serif;font-size:12px;font-weight:700;color:var(--gold);text-transform:uppercase;letter-spacing:1px}
.section-title{font-size:30px;font-weight:800;text-transform:uppercase;color:var(--ink);line-height:1.2}
.center{text-align:center}
.brand{display:flex;align-items:center;gap:8px;font-weight:700;font-size:20px;color:var(--gold)}
.brand-mark{width:14px;height:14px;background:var(--gold);flex:none}

/* top bar */
.topbar{height:34px;background:var(--dark);color:#ddd;font-size:11px;display:flex;align-items:center;justify-content:center;gap:28px}
.topbar span{display:flex;align-items:center;gap:6px}
.topbar svg{width:11px;height:11px;fill:var(--gold)}

/* nav */
.navbar{height:86px;display:flex;align-items:center;justify-content:space-between;padding:0 40px;border-bottom:1px solid var(--line)}
.nav{display:flex;gap:30px}
.nav a{font-size:13px;font-weight:600;color:var(--ink);text-decoration:none}
.nav a.active{color:var(--gold)}

/* hero */
.hero{position:relative;height:550px;background:linear-gradient(100deg,#5d6570 0%,#8b949c 40%,#b7bcc0 70%,#9aa1a8 100%)}
.hero-photo{position:absolute;inset:0;background:linear-gradient(90deg,rgba(40,46,54,.55) 0%,rgba(40,46,54,.1) 45%,rgba(40,46,54,.35) 100%)}
.hero-copy{position:absolute;left:520px;top:160px;width:440px}
.hero-copy h1{color:var(--gold);font-size:30px;font-weight:800;line-height:1.25}
.hero-copy .btn{margin-top:24px}
.hero-arrow{position:absolute;top:255px;width:30px;height:30px;fill:#fff;opacity:.8}
.hero-dots{position:absolute;bottom:20px;left:0;right:0;display:flex;justify-content:center;gap:8px}
.hero-dots i{width:8px;height:8px;border-radius:50%;background:rgba(255,255,255,.55)}
.hero-dots i.on{background:var(--gold)}

/* about */
.about{height:500px;position:relative;padding:70px 110px 0}
.about-copy{width:400px}
.about-copy .section-title{font-size:28px;margin:8px 0 16px}
.about-copy p{font-size:12px;color:var(--ink-soft)}
.about-tiles{display:flex;gap:14px;margin:22px 0}
.about-tile{flex:1;border:1px solid var(--line);padding:14px;display:flex;align-items:center;gap:10px;font-family:"Montserrat",Arial,sans-serif;font-size:12px;font-weight:700}
.about-tile i{width:26px;height:26px;border-radius:50%;background:var(--gold);flex:none}
.read-more{font-size:12px;font-weight:700;color:var(--gold);margin-top:16px;display:block}
.about-photo-frame{position:absolute;left:570px;top:90px;width:310px;height:310px;border:4px solid var(--gold)}
.about-photo{position:absolute;left:550px;top:70px;width:310px;height:310px;background:linear-gradient(135deg,#c9ccd0,#8e949b 60%,#6a7078)}

/* services */
.services{height:670px;background:var(--grey-band);padding-top:60px;position:relative}
.services p.lead{width:760px;margin:14px auto 0;font-size:12px;color:var(--ink-soft);text-align:center}
.services svg{position:absolute;left:0;top:150px}

/* portfolio */
.portfolio{height:1290px;padding-top:60px}
.portfolio .section-title{margin-top:6px}
.portfolio p.lead{width:800px;margin:14px auto 0;font-size:12px;color:var(--ink-soft);text-align:center}
.tabs{width:760px;margin:34px auto 0;display:flex;border-bottom:1px solid var(--line)}
.tabs span{padding:10px 18px;font-family:"Montserrat",Arial,sans-serif;font-size:11px;font-weight:700;color:var(--ink)}
.tabs span.active{color:var(--gold);border:1px solid var(--gold);border-bottom:3px solid var(--gold)}
.project-panel{width:760px;height:900px;margin:0 auto;border:1px solid var(--gold);border-top:none;display:grid;grid-template-columns:1fr 1fr;gap:40px 50px;padding:60px 70px}
.project-card{text-align:center;position:relative}
.project-photo{height:190px;background:linear-gradient(135deg,#cfd3d7,#8c939a)}
.project-icon{width:44px;height:44px;border-radius:50%;background:var(--gold);border:4px solid #fff;margin:-22px auto 0;position:relative}
.project-card h3{font-size:14px;font-weight:700;margin:10px 0 6px}
.project-card p{font-size:11px;color:var(--ink-soft);line-height:1.55}
.project-card .btn{margin-top:12px;font-size:10px;padding:7px 16px}

/* stats */
.stats{height:210px;background:var(--dark);display:flex;justify-content:space-around;align-items:center;padding:0 80px}
.stat{text-align:center;color:#fff}
.stat svg{width:34px;height:34px;fill:var(--gold)}
.stat-num{display:block;font-size:30px;font-weight:800;margin-top:4px}
.stat-label{font-size:11px;color:#ccc}

/* testimonials */
.testimonials{height:430px;padding-top:56px}
.quotes{display:flex;justify-content:center;gap:40px;margin-top:34px}
.quote{width:380px}
.quote-box{position:relative;background:var(--dark-2);color:#fff;font-size:12px;padding:28px 28px 28px 70px;height:150px}
.quote-mark{position:absolute;left:-12px;top:-14px;width:50px;height:50px;background:var(--gold);display:flex;align-items:center;justify-content:center}
.quote-mark svg{width:24px;height:24px;fill:#fff}
.quote-person{display:flex;align-items:center;gap:12px;margin-top:22px}
.avatar{width:44px;height:44px;border-radius:50%;background:linear-gradient(135deg,#c9a98f,#7d6a5d)}
.quote-person b{font-family:"Montserrat",Arial,sans-serif;font-size:14px;display:block}
.quote-person small{font-size:11px;color:var(--muted)}
.t-dots{display:flex;justify-content:center;gap:8px;margin-top:22px}
.t-dots i{width:8px;height:8px;border-radius:50%;background:#ccc}
.t-dots i.on{background:var(--gold)}

/* contact */
.contact{height:450px;position:relative;background:#f7f7f7}
.contact-copy{position:absolute;left:100px;top:110px;z-index:2;width:190px}
.contact-copy .section-title{font-size:30px;margin-top:4px;white-space:nowrap}
.contact-photo{position:absolute;left:310px;top:20px;width:320px;height:410px;background:linear-gradient(160deg,#e9ebee,#b8c0c8 55%,#dfe2e5)}
.contact-form{position:absolute;left:640px;top:20px;width:250px;height:410px;background:var(--dark);padding:30px 22px}
.field{height:34px;background:#fff;margin-bottom:14px;font-size:11px;color:var(--muted);padding:8px 10px}
.field.area{height:100px}
.contact-form .btn{width:100%;text-align:center}

/* footer */
.footer{height:390px;padding:60px 60px 0;display:grid;grid-template-columns:1.4fr 1fr 1fr 1fr 1.2fr;gap:24px;border-top:1px solid var(--line)}
.footer p,.footer li{font-size:11px;color:var(--ink-soft);list-style:none;line-height:2}
.footer h4{font-size:13px;font-weight:700;margin-bottom:10px}
.footer .brand{font-size:17px;margin-bottom:14px}
.socials{display:flex;gap:8px;margin-top:16px}
.socials i{width:22px;height:22px;background:var(--gold)}
.contact-line{display:flex;gap:8px;align-items:flex-start;overflow-wrap:anywhere}
.contact-line i{width:10px;height:10px;background:var(--gold);border-radius:50%;margin-top:6px;flex:none}
</style>
</head>
<body>
<div class="site">

  <div class="topbar">
    <span><svg viewBox="0 0 10 10"><path d="M5 0a3.5 3.5 0 0 0-3.5 3.5C1.5 6 5 10 5 10s3.5-4 3.5-6.5A3.5 3.5 0 0 0 5 0z"/></svg>Quorva Advisory GmbH, Lindenweg 14, 60311 Frankfurt</span>
    <span><svg viewBox="0 0 10 10"><path d="M2 0l2 2.5-1 1.2a6 6 0 0 0 3.3 3.3l1.2-1L10 8l-1.5 2C4 10 0 6 0 1.5z"/></svg>+49 69 4471 2280</span>
    <span><svg viewBox="0 0 10 10"><path d="M2 0l2 2.5-1 1.2a6 6 0 0 0 3.3 3.3l1.2-1L10 8l-1.5 2C4 10 0 6 0 1.5z"/></svg>+49 69 4471 2281</span>
    <span><svg viewBox="0 0 10 10"><path d="M0 2h10v6H0zM0 2l5 3.5L10 2" fill="none" stroke="#f4b400"/></svg>info@quorva-advisory.com</span>
  </div>

  <header class="navbar">
    <div class="brand"><i class="brand-mark"></i>Quorva Advisory</div>
    <nav class="nav">
      <a class="active">Home</a><a>About Us</a><a>Services ▾</a><a>Portfolio ▾</a><a>Contact Us</a>
    </nav>
    <span class="btn">Let's Talk</span>
  </header>

  <section class="hero">
    <div class="hero-photo" role="img" aria-label="Business consultant in a suit holding a tablet in a bright modern office"></div>
    <svg class="hero-arrow" style="left:14px" viewBox="0 0 30 30"><path d="M19 6 10 15l9 9" fill="none" stroke="#fff" stroke-width="3"/></svg>
    <svg class="hero-arrow" style="right:14px" viewBox="0 0 30 30"><path d="M11 6l9 9-9 9" fill="none" stroke="#fff" stroke-width="3"/></svg>
    <div class="hero-copy">
      <h1>With Quorva Advisory You Create The Best Conditions For IT Systems That Do What They Should.</h1>
      <span class="btn">Read More</span>
    </div>
    <div class="hero-dots"><i class="on"></i><i></i><i></i></div>
  </section>

  <section class="about">
    <div class="about-copy">
      <span class="eyebrow">About Us</span>
      <h2 class="section-title">Welcome to Quorva<br>Advisory GmbH</h2>
      <p>We guide IT decision makers through strategy, transformation and quality. Our agile teams bring clarity to complex systems, align technology with business goals and deliver results that last.</p>
      <div class="about-tiles">
        <div class="about-tile"><i></i>Our Mission</div>
        <div class="about-tile"><i></i>Our Vision</div>
      </div>
      <p>Every engagement starts with listening. We shape clear roadmaps and stay with you until systems run exactly as planned.</p>
      <span class="read-more">Read More →</span>
    </div>
    <div class="about-photo-frame"></div>
    <div class="about-photo" role="img" aria-label="Consultants meeting around a table in a glass office"></div>
  </section>

  <section class="services">
    <div class="center">
      <span class="eyebrow">Services</span>
      <h2 class="section-title" style="margin-top:6px">Solutions We Offer!</h2>
    </div>
    <p class="lead">From first strategy workshop to stable operation, we cover every stage of your IT landscape with focused expertise, transparent methods and a clear view on quality and value.</p>
    <svg width="1000" height="520" viewBox="0 0 1000 520">
      <path d="M433 73 A190 190 0 0 1 433 447" fill="none" stroke="#3a3a3a" stroke-width="2" stroke-dasharray="6 6"/>
      <circle cx="400" cy="260" r="140" fill="none" stroke="#cfcfcf" stroke-width="14"/>
      <circle cx="400" cy="260" r="110" fill="#fff" stroke="#f4b400" stroke-width="5"/>
      <rect x="312" y="238" width="14" height="14" fill="#f4b400"/>
      <text x="334" y="252" font-family="Montserrat, Arial, sans-serif" font-size="17" font-weight="700" fill="#f4b400">Quorva Advisory</text>
      <g font-family="Montserrat, Arial, sans-serif" font-size="13" font-weight="600" fill="#2f2f2f">
        <circle cx="495" cy="95" r="17" fill="#f4b400"/><circle cx="495" cy="95" r="6" fill="#fff"/>
        <text x="522" y="100">IT Strategy Consulting</text>
        <circle cx="565" cy="165" r="17" fill="#f4b400"/><rect x="559" y="159" width="12" height="12" fill="#fff"/>
        <text x="592" y="170">Project Management</text>
        <circle cx="590" cy="260" r="17" fill="#f4b400"/><path d="M582 260h16M592 254l6 6-6 6" stroke="#fff" stroke-width="2.5" fill="none"/>
        <text x="617" y="265">Digital Transformation</text>
        <circle cx="565" cy="355" r="17" fill="#f4b400"/><path d="M558 355l5 5 9-10" stroke="#fff" stroke-width="2.5" fill="none"/>
        <text x="592" y="360">Task Management</text>
        <circle cx="495" cy="425" r="17" fill="#f4b400"/><path d="M495 416l3 6 6 1-4.5 4 1 6-5.5-3-5.5 3 1-6-4.5-4 6-1z" fill="#fff"/>
        <text x="522" y="430">IT Quality Management</text>
      </g>
    </svg>
  </section>

  <section class="portfolio">
    <div class="center">
      <span class="eyebrow">Portfolio</span>
      <h2 class="section-title">Quorva Advisory Specializes in Complex Projects</h2>
    </div>
    <p class="lead">Our range of services covers the management of the entire development process, from requirements and architecture to rollout, always with quality and clear communication at the core.</p>
    <p class="lead">We support large programmes in telecommunication, automotive and IT provider environments, combining agile delivery with structured governance so that every milestone is reached on time and within budget.</p>
    <div class="tabs">
      <span class="active">Programme Excellence</span><span>Consulting &amp; Excellence</span><span>Digitalization</span><span>Cloud Transition</span>
    </div>
    <div class="project-panel">
      <div class="project-card">
        <div class="project-photo" role="img" aria-label="Team discussing a project plan at a desk"></div>
        <div class="project-icon"></div>
        <h3>Excellent Project Management</h3>
        <p>Structured planning, clear ownership and steady reporting keep complex programmes on course from kickoff to handover.</p>
        <span class="btn">Learn More</span>
      </div>
      <div class="project-card">
        <div class="project-photo" role="img" aria-label="Colleagues reviewing documents in a meeting room"></div>
        <div class="project-icon"></div>
        <h3>Excellent Quality</h3>
        <p>We define measurable standards, test early and often, and make sure every release meets what your business expects.</p>
        <span class="btn">Learn More</span>
      </div>
      <div class="project-card">
        <div class="project-photo" role="img" aria-label="Business people working together at a conference table"></div>
        <div class="project-icon"></div>
        <h3>Excellent Commissioning</h3>
        <p>Smooth go-live through careful preparation, stable migration paths and close support for your teams on day one.</p>
        <span class="btn">Learn More</span>
      </div>
      <div class="project-card">
        <div class="project-photo" role="img" aria-label="Consultant presenting results to a client"></div>
        <div class="project-icon"></div>
        <h3>Excellent Service For Regular Operations</h3>
        <p>Reliable operation after launch with monitoring, continuous improvement and a partner who knows your systems well.</p>
        <span class="btn">Learn More</span>
      </div>
    </div>
  </section>

  <section class="stats">
    <div class="stat"><svg viewBox="0 0 34 34"><rect x="3" y="8" width="28" height="20" rx="2"/><rect x="12" y="4" width="10" height="6" fill="none" stroke="#f4b400" stroke-width="2"/></svg><span class="stat-num">352</span><span class="stat-label">Projects Completed</span></div>
    <div class="stat"><svg viewBox="0 0 34 34"><circle cx="12" cy="11" r="5"/><circle cx="23" cy="11" r="5"/><path d="M2 30c0-7 5-11 10-11s10 4 10 11zM14 30c0-7 4-11 9-11s9 4 9 11z"/></svg><span class="stat-num">350+</span><span class="stat-label">Happy Clients</span></div>
    <div class="stat"><svg viewBox="0 0 34 34"><path d="M8 4h18v8a9 9 0 0 1-18 0zM15 20h4v6h5v4H10v-4h5z"/></svg><span class="stat-num">12</span><span class="stat-label">Awards Received</span></div>
    <div class="stat"><svg viewBox="0 0 34 34"><circle cx="17" cy="17" r="14"/><path d="M17 9v9l6 4" stroke="#353535" stroke-width="2.5" fill="none"/></svg><span class="stat-num">15</span><span class="stat-label">Years of Service</span></div>
  </section>

  <section class="testimonials">
    <div class="center">
      <span class="eyebrow">Testimonials</span>
      <h2 class="section-title" style="margin-top:6px">Check What Our Clients Say</h2>
    </div>
    <div class="quotes">
      <div class="quote">
        <div class="quote-box">
          <span class="quote-mark"><svg viewBox="0 0 24 24"><path d="M2 20v-7c0-5 3-8 7-9v3c-2 1-3 3-3 5h3v8zm12 0v-7c0-5 3-8 7-9v3c-2 1-3 3-3 5h3v8z"/></svg></span>
          The team brought real structure into our migration programme. Clear reporting, honest advice and a result that exceeded what our board expected from the start.
        </div>
        <div class="quote-person"><span class="avatar" role="img" aria-label="Client portrait"></span><div><b>Mara Lindqvist</b><small>IT Procurement Lead</small></div></div>
      </div>
      <div class="quote">
        <div class="quote-box">
          <span class="quote-mark"><svg viewBox="0 0 24 24"><path d="M2 20v-7c0-5 3-8 7-9v3c-2 1-3 3-3 5h3v8zm12 0v-7c0-5 3-8 7-9v3c-2 1-3 3-3 5h3v8z"/></svg></span>
          Agile, focused and always reachable. Their quality management gave us the confidence to launch on schedule across all of our regional sites.
        </div>
        <div class="quote-person"><span class="avatar" role="img" aria-label="Client portrait"></span><div><b>Tobias Renn</b><small>Head of IT</small></div></div>
      </div>
    </div>
    <div class="t-dots"><i class="on"></i><i></i><i></i></div>
  </section>

  <section class="contact">
    <div class="contact-photo" role="img" aria-label="Smiling businessman working on a laptop"></div>
    <div class="contact-copy">
      <span class="eyebrow">Get In Touch</span>
      <h2 class="section-title">Message Us</h2>
    </div>
    <form class="contact-form">
      <div class="field">Your Name</div>
      <div class="field">Email Address</div>
      <div class="field">Phone Number</div>
      <div class="field area">Your Message</div>
      <span class="btn">Send Message</span>
    </form>
  </section>

  <footer class="footer">
    <div>
      <div class="brand"><i class="brand-mark"></i>Quorva Advisory</div>
      <p>Independent IT consulting for strategy, digital transformation and quality management, built on agile teamwork and long-term partnership.</p>
      <div class="socials"><i></i><i></i><i></i><i></i></div>
    </div>
    <div>
      <h4>Our Company</h4>
      <ul><li>Web Service</li><li>About Company</li><li>Services We Provide</li><li>Meet Our Team</li></ul>
    </div>
    <div>
      <h4>Important Links</h4>
      <ul><li>Home</li><li>About Us</li><li>Services</li><li>Portfolio</li><li>Contact</li></ul>
    </div>
    <div>
      <h4>Our Services</h4>
      <ul><li>IT Strategy Consulting</li><li>Digital Transformation</li><li>IT Quality Management</li></ul>
    </div>
    <div>
      <h4>Our Contacts</h4>
      <p class="contact-line"><i></i>Quorva Advisory GmbH, Lindenweg 14, 60311 Frankfurt</p>
      <p class="contact-line"><i></i>info@quorva-advisory.com</p>
      <p class="contact-line"><i></i>+49 69 4471 2280</p>
      <p class="contact-line"><i></i>+49 69 4471 2281</p>
    </div>
  </footer>

</div>
</body>
</html>
```